Business Card for Managing Partner Investment Fund

To create a business card template for an investment fund manager. Business card should be more professional in nature, not too colorful, more upscale, and created using the attached logos and fund name files. I would prefer a black or gray color scheme, but am open to the use of color as well. I would prefer a double sided business card, but open to single sided business card designs as well. The business card should include: name, title, and contact information, as well as logo and company name. I would prefer a more stream-lined, simple business card design.
Updates
Address: 4190 NE 38th Ter. Ocala, FL 34470
Email: talvin47@quorimail.net
Phone: 561-347-9162
Title: managing partner
Name: Dorian Velsky
Fund Name: Ambergate Capital
Logos can be found in files attached to the brief
Target Market(s)
potential investors, other fund managers
Industry/Entity Type
Finance
Contact Information for Business Card
Name on card: Dorian Velsky
Title: Managing Partner
Colors
Designer to choose colors to be used in the design.
Requirements
Must have
- Phone number
- email address
- physical address
- title
- name
- logo
- Fund name
Nice to have
- simple layout
Should not have
- too many colors, busy fonts,

```html
<!DOCTYPE html>
<html lang="en">
<head>
<meta charset="utf-8">
<title>Ambergate Capital – Business Card</title>
<link href="https://fonts.googleapis.com/css2?family=Montserrat:wght@400;500;700&display=swap" rel="stylesheet">
<style>
  :root {
    --navy: #1d4466;
    --navy-deep: #173a59;
    --shard-yellow: #d9d44a;
    --paper: #f4f4f2;
    --ink: #1a1a1a;
    --ink-soft: #3a3a3a;
    --muted: #8a8a8a;
    --backdrop: #e3e4e2;
  }
  * { box-sizing: border-box; margin: 0; padding: 0; }
  html, body { width: 1200px; height: 900px; overflow: hidden; }
  body {
    background: var(--backdrop);
    font-family: "Montserrat", sans-serif;
    display: flex;
    flex-direction: column;
    align-items: center;
    justify-content: center;
    gap: 30px;
  }
  .card {
    position: relative;
    width: 700px;
    height: 400px;
    overflow: hidden;
    box-shadow: 0 6px 18px rgba(0,0,0,.18);
  }
  .card__pattern {
    position: absolute;
    inset: 0;
    background: linear-gradient(135deg, var(--navy) 0%, #3f6a5c 35%, var(--shard-yellow) 55%, #3f6a5c 75%, var(--navy) 100%);
  }
  .front__panel {
    position: absolute;
    left: 20%;
    top: 22%;
    width: 52%;
    height: 56%;
    background: var(--navy-deep);
    display: flex;
    align-items: center;
    justify-content: center;
  }
  .wordmark {
    display: flex;
    align-items: center;
    gap: 12px;
    font-weight: 500;
    letter-spacing: .14em;
    text-transform: uppercase;
  }
  .wordmark__mark { width: 18px; height: 18px; }
  .wordmark--light { color: #ffffff; font-size: 26px; }
  .wordmark--light .wordmark__mark { background: #ffffff; }
  .wordmark--dark { color: var(--ink); font-size: 19px; }
  .wordmark--dark .wordmark__mark { background: var(--ink); width: 14px; height: 14px; }
  .back__panel {
    position: absolute;
    left: 6%;
    top: 8%;
    right: 4%;
    bottom: 12%;
    background: var(--paper);
    display: flex;
    align-items: center;
    padding: 0 40px 0 40px;
  }
  .back__brand { width: 48%; display: flex; justify-content: center; }
  .contact { width: 52%; padding-left: 10px; }
  .contact__name {
    color: var(--navy);
    font-weight: 700;
    font-size: 21px;
    letter-spacing: .01em;
    text-transform: uppercase;
  }
  .contact__title { color: var(--muted); font-size: 15px; margin-top: 4px; }
  .contact__address { color: var(--ink-soft); font-size: 14px; line-height: 1.85; margin-top: 18px; }
  .contact__lines { margin-top: 18px; font-size: 14px; color: var(--ink-soft); line-height: 1.85; }
  .contact__label { font-weight: 700; color: var(--ink); margin-right: 4px; }
</style>
</head>
<body>
  <section class="card card--front">
    <div class="card__pattern" role="img" aria-label="Navy and yellow shattered-shard pattern"></div>
    <div class="front__panel">
      <div class="wordmark wordmark--light"><span class="wordmark__mark"></span>Ambergate Capital</div>
    </div>
  </section>

  <section class="card card--back">
    <div class="card__pattern" role="img" aria-label="Navy and yellow shattered-shard pattern"></div>
    <div class="back__panel">
      <div class="back__brand">
        <div class="wordmark wordmark--dark"><span class="wordmark__mark"></span>Ambergate Capital</div>
      </div>
      <div class="contact">
        <h1 class="contact__name">Dorian Velsky</h1>
        <p class="contact__title">Managing Partner</p>
        <p class="contact__address">4190 NE 38th Ter.<br>Ocala<br>FL 34470</p>
        <p class="contact__lines">
          <span class="contact__label">Phone:</span>561-347-9162<br>
          <span class="contact__label">Email:</span>talvin47@quorimail.net
        </p>
      </div>
    </div>
  </section>
</body>
</html>
```